Sophisticated, clean website reflecting my feminine, playful side to sell my abstract art,

I need a website no more than 3 pages to showcase my paintings, a little about me and some contact info. I do abstracts so looking for something a little edgy, yet feminine and current.
Updates

Hi there, These are some artists websites that I Iike: Mirabelvoss.com (I like how airy it is) tobiasmerrowind.com kevinplodderas.com (I like how it scrolls) I'll need a place for a photo ( a headshot-i do not have it yet so I'll need to be able to upload that later) as well as an area for my bio. Also, it's important that I will be able to upload any new photos and descriptions easily so it should be user friendly. Lastly, I like in a sunny place so would like to have this seem upbeat and playful as that is how i like to paint. thanks-I'm trying to upload my photos now -

Target Market(s)

ppl ages 35-70 who want large scale art for their homes

Industry/Entity Type

art

Coding

Coded - Design and coding required

Number of Pages Required

3 page

Colors

Designer to choose colors to be used in the design.

Requirements
Must have
• photos of my art, a place for my bio, be easy to reach me. tasteful-nothing too "in your face" -my clients are pretty high end and organized. They like clean lines
Nice to have
• sophisticated background, muted tones in the back-similar clean font throughout-no cursive
Should not have
• too many dark areas. Too many blocks of color. Too serious.

```html
<!DOCTYPE html>
<html lang="en">
<head>
<meta charset="utf-8">
<title>Marlena Quist — Abstract Art</title>
<link rel="stylesheet" href="https://fonts.googleapis.com/css2?family=Questrial&family=Mulish:wght@300;400&display=swap">
<style>
  :root {
    --page-bg: #f2f2f2;
    --ink: #4a4a4a;
    --ink-soft: #5c5c5c;
    --ink-dark: #222222;
    --rule: #9a9a9a;
    --rule-light: #b5b5b5;
    --frame: #ffffff;
    --photo-grey: #dedede;
    --arrow: #6a6a6a;
    --arrow-light: #f4f0f0;
  }
  * { box-sizing: border-box; margin: 0; padding: 0; }
  html, body { width: 1200px; height: 2824px; overflow: hidden; }
  body {
    position: relative;
    background: linear-gradient(to bottom, var(--page-bg) 0, var(--page-bg) 2700px, #f7f7f7 2824px);
    color: var(--ink);
    font-family: "Mulish", sans-serif;
  }

  /* Header */
  .site-header { position: absolute; top: 0; left: 0; width: 1200px; height: 169px; }
  .brand {
    position: absolute; top: 32px; left: 0; width: 1200px;
    display: flex; justify-content: center; align-items: center; gap: 18px;
    font-family: "Questrial", sans-serif; font-size: 46px; letter-spacing: 1px;
    color: var(--ink-soft);
  }
  .brand-mark { width: 24px; height: 38px; background: var(--ink-soft); }
  .header-rule { position: absolute; top: 110px; left: 0; width: 1200px; height: 1px; background: var(--rule); }
  .main-nav {
    position: absolute; top: 128px; left: 0; width: 1200px;
    display: flex; justify-content: center; align-items: center;
    font-family: "Questrial", sans-serif; font-size: 17px; color: var(--ink);
  }
  .main-nav a { color: inherit; text-decoration: none; }
  .nav-dot { width: 4px; height: 4px; background: #9a9a9a; margin: 0 55px; }

  /* Hero */
  .hero { position: absolute; top: 169px; left: 0; width: 1200px; height: 662px; }
  .hero-art {
    width: 100%; height: 100%;
    background:
      radial-gradient(ellipse 220px 180px at 640px 320px, #8a4a3a 0%, rgba(138,74,58,0) 70%),
      radial-gradient(ellipse 420px 320px at 600px 330px, #d79fbf 0%, rgba(215,159,191,0) 75%),
      radial-gradient(ellipse 300px 260px at 150px 420px, #a2442c 0%, rgba(162,68,44,0) 70%),
      radial-gradient(ellipse 280px 240px at 1080px 200px, #b5603e 0%, rgba(181,96,62,0) 70%),
      linear-gradient(120deg, #d8a6b8 0%, #c98a8f 35%, #e0b9c6 60%, #c27a6a 100%);
  }
  .carousel-arrow { position: absolute; }
  .hero .carousel-arrow { top: 296px; }

  /* Section headings */
  .section-title {
    position: absolute; left: 0; width: 1200px; text-align: center;
    font-family: "Questrial", sans-serif; font-weight: 400; color: var(--ink-soft);
    line-height: 1;
  }
  .section-title span {
    display: inline-block; padding: 14px 4px 10px;
    border-top: 3px solid var(--rule-light); border-bottom: 3px solid var(--rule-light);
  }
  .about-title { top: 895px; font-size: 54px; }
  .gallery-title { top: 1537px; font-size: 47px; }
  .contact-title { top: 2292px; font-size: 55px; }

  /* About */
  .portrait-frame {
    position: absolute; top: 1049px; left: 98px; width: 328px; height: 382px;
    background: var(--frame); box-shadow: 2px 3px 6px rgba(0,0,0,0.12);
  }
  .portrait {
    position: absolute; top: 0; left: 0; width: 318px; height: 374px;
    background: radial-gradient(ellipse 140px 200px at 160px 200px, #c9c4c0 0%, var(--photo-grey) 80%);
  }
  .bio { position: absolute; top: 1056px; left: 477px; width: 640px; color: var(--ink-dark); }
  .bio p { font-size: 19.5px; line-height: 27.5px; font-weight: 300; margin-bottom: 14px; }
  .bio .bio-lead { font-size: 23.5px; line-height: 28px; font-weight: 400; margin-bottom: 12px; }

  /* Gallery */
  .gallery-frame {
    position: absolute; top: 1639px; left: 133px; width: 928px; height: 546px;
    background: var(--frame); padding: 9px; box-shadow: 1px 2px 5px rgba(0,0,0,0.1);
  }
  .gallery-art {
    width: 100%; height: 100%;
    background:
      radial-gradient(ellipse 180px 150px at 470px 360px, #1f1d1c 0%, rgba(31,29,28,0) 75%),
      radial-gradient(ellipse 260px 200px at 760px 230px, #e9e2d3 0%, rgba(233,226,211,0) 75%),
      radial-gradient(ellipse 220px 200px at 330px 170px, #1f7b82 0%, rgba(31,123,130,0) 75%),
      radial-gradient(ellipse 220px 200px at 110px 200px, #c56a2a 0%, rgba(197,106,42,0) 75%),
      linear-gradient(110deg, #d1772f 0%, #2f8d86 35%, #2a2a2a 55%, #c97a3a 75%, #dcd3bb 100%);
  }
  .gallery .carousel-arrow { top: 1883px; }

  /* Contact */
  .contact-intro {
    position: absolute; top: 2412px; left: 0; width: 1200px; text-align: center;
    font-size: 21px; font-weight: 300; color: var(--ink-dark);
  }
  .contact-list { position: absolute; top: 2478px; left: 0; width: 1200px; list-style: none; }
  .contact-item {
    position: absolute; left: 0; width: 1200px;
    display: flex; justify-content: center; align-items: center; gap: 8px;
    font-size: 17px; color: var(--ink-dark);
  }
  .contact-item:nth-child(1) { top: 0; }
  .contact-item:nth-child(2) { top: 50px; }
  .contact-item:nth-child(3) { top: 98px; }
  .contact-item:nth-child(4) { top: 148px; }
  .contact-icon { width: 26px; height: 26px; }
  .social-dot { width: 22px; height: 22px; border: 1.5px solid var(--ink-dark); border-radius: 50%; }

  .site-footer {
    position: absolute; top: 2773px; left: 0; width: 1200px; text-align: center;
    font-family: "Questrial", sans-serif; font-size: 14px; color: var(--ink-soft);
  }
</style>
</head>
<body>
  <header class="site-header">
    <div class="brand"><span>MARLENA</span><span class="brand-mark"></span><span>QUIST</span></div>
    <div class="header-rule"></div>
    <nav class="main-nav">
      <a href="#home">HOME</a><span class="nav-dot"></span>
      <a href="#about">ABOUT ME</a><span class="nav-dot"></span>
      <a href="#gallery">GALLERY</a><span class="nav-dot"></span>
      <a href="#contact">CONTACT</a>
    </nav>
  </header>

  <section class="hero" id="home">
    <div class="hero-art" role="img" aria-label="Abstract painting of a pink and rust rose with dark brush strokes"></div>
    <svg class="carousel-arrow" style="left:36px" width="28" height="48" viewBox="0 0 28 48"><polyline points="24,4 6,24 24,44" fill="none" stroke="var(--arrow-light)" stroke-width="3"/></svg>
    <svg class="carousel-arrow" style="left:1122px" width="28" height="48" viewBox="0 0 28 48"><polyline points="4,4 22,24 4,44" fill="none" stroke="var(--arrow-light)" stroke-width="3"/></svg>
  </section>

  <section class="about" id="about">
    <h2 class="section-title about-title"><span>ABOUT ME</span></h2>
    <div class="portrait-frame">
      <div class="portrait" role="img" aria-label="Headshot portrait of the artist"></div>
    </div>
    <div class="bio">
      <p class="bio-lead">Lorem ipsum dolor sit amet, consectetur adipiscing elit, sed do eiusmod tempor incididunt ut labore et dolore.</p>
      <p>Ut enim ad minim veniam, quis nostrud exercitation Lorem ipsum dolor sit amet, consectetur adipiscing elit, sed do eiusmod tempor</p>
      <p>Duis aute irure dolor in reprehenderit in voluptate velit esse cillum dolore eu fugiat nulla pariatur. Excepteur sint occaecat cupidatat non proident, sunt in culpa qui officia deserunt mollit anim id est laborum.</p>
      <p>Sed ut perspiciatis unde pariatur. Excepteur sint occaecat cupidatat non proident, sunt in culpa qui officia deserunt mollit nt ut labore et dolore magna aliqua. Ut enim ad minim veniam, quis nostrud exercitation Lorem ipsum dolor sit amet, consectetur adipiscing elit, sed do.</p>
    </div>
  </section>

  <section class="gallery" id="gallery">
    <h2 class="section-title gallery-title"><span>GALLERY</span></h2>
    <svg class="carousel-arrow" style="left:66px" width="30" height="50" viewBox="0 0 30 50"><polyline points="26,4 6,25 26,46" fill="none" stroke="var(--arrow)" stroke-width="4"/></svg>
    <div class="gallery-frame">
      <div class="gallery-art" role="img" aria-label="Abstract painting with teal, orange, black and cream brush strokes"></div>
    </div>
    <svg class="carousel-arrow" style="left:1104px" width="30" height="50" viewBox="0 0 30 50"><polyline points="4,4 24,25 4,46" fill="none" stroke="var(--arrow)" stroke-width="4"/></svg>
  </section>

  <section class="contact" id="contact">
    <h2 class="section-title contact-title"><span>CONTACT ME</span></h2>
    <p class="contact-intro">Please get in touch with me on below details.</p>
    <ul class="contact-list">
      <li class="contact-item">
        <svg class="contact-icon" viewBox="0 0 26 26"><rect x="1.5" y="5.5" width="23" height="15" fill="none" stroke="var(--ink-dark)" stroke-width="1.2"/><polyline points="1.5,5.5 13,15 24.5,5.5" fill="none" stroke="var(--ink-dark)" stroke-width="1.2"/><line x1="1.5" y1="20.5" x2="10" y2="12.5" stroke="var(--ink-dark)" stroke-width="1.2"/><line x1="24.5" y1="20.5" x2="16" y2="12.5" stroke="var(--ink-dark)" stroke-width="1.2"/></svg>
        <span>info@marlenaquist.com</span>
      </li>
      <li class="contact-item">
        <svg class="contact-icon" viewBox="0 0 26 26"><path d="M5 3 L9 3 L11 8 L8.5 10 C10 14 12 16 16 17.5 L18 15 L23 17 L23 21 C23 22.5 21.5 23.5 20 23.3 C11 22 4 15 2.7 6 C2.5 4.5 3.5 3 5 3 Z" fill="none" stroke="var(--ink-dark)" stroke-width="1.2"/><path d="M15 3 A8 8 0 0 1 23 11" fill="none" stroke="var(--ink-dark)" stroke-width="1.2"/><path d="M15 7 A4 4 0 0 1 19 11" fill="none" stroke="var(--ink-dark)" stroke-width="1.2"/></svg>
        <span>Phone: (555) 014 2286</span>
      </li>
      <li class="contact-item">
        <span class="social-dot"></span>
        <span>social @mquistart</span>
      </li>
      <li class="contact-item">
        <span class="social-dot"></span>
        <span>videos @mqpainter</span>
      </li>
    </ul>
  </section>

  <footer class="site-footer">© 2022 Marlena Quist &nbsp; All Rights Reserved</footer>
</body>
</html>
```